Speisekarten für griechisches Restaurant
Zielgruppe
modernes griechisches Restaurant
Aufgabenstellung
neues modernen helles design ,
nach Durchsicht aus meinen Vorlangen, sollten ein paar Anpassung am text und preisen noch durchgeführt werden.
aus der pdf datei,, ist ab Seite 7 die richtige Speisekarte,, vorher sind nur entwürfe vom mir, diese bitte ignorieren.

```html
<!DOCTYPE html>
<html lang="de">
<head>
<meta charset="utf-8">
<title>Tiganakia – Speisekarte</title>
<link href="https://fonts.googleapis.com/css2?family=Bebas+Neue&family=Playfair+Display:wght@500;600&family=Figtree:wght@400;500&display=swap" rel="stylesheet">
<style>
  :root {
    --leaf: #8dbb3c;
    --olive: #5a8650;
    --olive-box: #5f8b5b;
    --ink: #111111;
    --paper: #ffffff;
    --stage: #e9e9e7;
    --wood-dark: #3b2a1f;
    --wood-mid: #6b4a32;
    --highlight: #e6f0c8;
  }
  html, body {
    margin: 0;
    padding: 0;
    width: 1200px;
    height: 1117px;
    overflow: hidden;
    background: var(--stage);
  }
  .menu-page {
    position: absolute;
    left: 220px;
    top: 21px;
    width: 1024px;
    height: 1448px;
    background: var(--paper);
    transform: scale(0.742);
    transform-origin: 0 0;
    font-family: "Figtree", sans-serif;
    color: var(--ink);
    overflow: hidden;
  }
  .hero { position: absolute; left: 0; top: 0; width: 916px; height: 430px; }
  .key-border { position: absolute; left: 930px; top: 10px; width: 82px; height: 1428px; }

  .title {
    position: absolute; left: 70px; top: 428px; margin: 0;
    font-family: "Playfair Display", serif; font-weight: 600;
    font-size: 80px; letter-spacing: 1px; color: var(--olive); line-height: 1;
  }
  .title-tag {
    position: absolute; left: 500px; top: 444px; width: 407px; height: 61px;
    background: var(--leaf); color: var(--paper);
    font-family: "Playfair Display", serif; font-weight: 500; font-size: 36px;
    display: flex; align-items: center; justify-content: center; letter-spacing: .5px;
  }

  .section-heading {
    font-family: "Bebas Neue", sans-serif; font-weight: 400;
    margin: 0; line-height: 40px;
  }
  .col-left { position: absolute; left: 83px; top: 548px; width: 372px; }
  .col-left .section-heading { color: var(--olive); font-size: 44px; }
  .heading-rule { display: block; margin: 14px 0 30px; }

  .dish { position: relative; padding-bottom: 14px; margin-bottom: 16px; }
  .col-left .dish { border-bottom: 2px solid var(--leaf); }
  .col-left .dish:last-child { border-bottom: none; }
  .dish-name {
    font-family: "Bebas Neue", sans-serif; font-size: 34px; line-height: 34px;
    color: var(--leaf); margin: 0;
  }
  .dish-price {
    position: absolute; right: 2px; top: -6px;
    font-family: "Bebas Neue", sans-serif; font-size: 36px; color: var(--ink);
    padding: 0 8px 0 22px;
    background: linear-gradient(to bottom, transparent 45%, var(--highlight) 45%, var(--highlight) 85%, transparent 85%);
  }
  .dish-desc { margin: 0; font-size: 19px; line-height: 21px; }
  .dish-desc + .dish-desc { margin-top: 12px; }
  .allergens { font-size: 10px; color: var(--leaf); letter-spacing: 2px; margin-left: 16px; }

  .note-box {
    position: absolute; left: 0; top: 1196px; width: 494px; height: 116px;
    background: var(--olive-box); color: var(--paper);
    box-sizing: border-box; padding: 20px 30px 0 83px;
    font-size: 21px; line-height: 26px;
  }

  .col-right {
    position: absolute; left: 494px; top: 545px; width: 413px; height: 528px;
    background: var(--ink); color: var(--paper);
    box-sizing: border-box; padding: 28px 35px 0 32px;
  }
  .col-right .section-heading { font-size: 42px; line-height: 40px; margin-bottom: 22px; }
  .col-right .section-heading span { color: var(--leaf); }
  .col-right .dish { border-bottom: 2px solid #d9d9d9; margin-bottom: 14px; padding-bottom: 14px; }
  .col-right .dish:last-child { border-bottom: none; }
  .col-right .dish-name { color: var(--paper); font-size: 33px; margin-bottom: 6px; }
  .col-right .dish-price { background: none; color: var(--leaf); padding: 0; right: 0; top: -4px; }
  .col-right .dish-desc { font-size: 19px; line-height: 21px; }

  .brand {
    position: absolute; left: 540px; top: 1110px; width: 340px;
    display: flex; flex-direction: column; align-items: center; gap: 18px;
  }
  .brand-mark { width: 106px; height: 106px; border-radius: 50%; border: 8px solid var(--olive); box-sizing: border-box; }
  .brand-name { font-family: "Figtree", sans-serif; font-weight: 500; font-size: 64px; color: var(--olive); line-height: 1; }

  .footer-note {
    position: absolute; left: 0; top: 1366px; width: 930px;
    text-align: center; font-size: 18px; color: var(--ink);
  }
</style>
</head>
<body>
<main class="menu-page">

  <svg class="hero" viewBox="0 0 916 430" role="img" aria-label="Foto: griechische Salate und Vorspeisen auf einem Holztisch">
    <defs>
      <linearGradient id="woodTone" x1="0" y1="0" x2="1" y2="1">
        <stop offset="0" stop-color="#4a3324"/>
        <stop offset=".5" stop-color="#6b4a32"/>
        <stop offset="1" stop-color="#2f2219"/>
      </linearGradient>
      <clipPath id="heroClip">
        <path d="M0 0H916V330C760 380 560 395 330 390C170 386 70 360 0 330Z"/>
      </clipPath>
    </defs>
    <rect width="916" height="430" fill="url(#woodTone)" clip-path="url(#heroClip)"/>
    <path d="M0 300C120 320 260 345 420 345C620 345 780 320 916 330V338C760 372 560 392 360 388C190 384 80 360 0 335Z" fill="var(--leaf)"/>
  </svg>

  <svg class="key-border" viewBox="0 0 82 1428" role="img" aria-label="Griechisches Mäanderband als Randverzierung">
    <rect x="0" y="0" width="10" height="1428" fill="var(--leaf)"/>
    <rect x="22" y="0" width="60" height="1428" fill="var(--leaf)" opacity=".75"/>
  </svg>

  <h1 class="title">TIGANAKIA</h1>
  <div class="title-tag">(PFANNENGERICHTE)</div>

  <section class="col-left">
    <h2 class="section-heading">Diese Gerichte werden<br>von Salat und Patatakia<br>begleitet!</h2>
    <svg class="heading-rule" width="356" height="12" viewBox="0 0 356 12">
      <path d="M0 3H354M110 9L210 6" stroke="var(--leaf)" stroke-width="3" fill="none" stroke-linecap="round"/>
    </svg>

    <article class="dish">
      <h3 class="dish-name">Kavaxa</h3>
      <span class="dish-price">21,5,-</span>
      <p class="dish-desc">Schweinefilet-Medaillons mit frischen Champignons und Sauce nach Wahl,</p>
      <p class="dish-desc">Kavaxa- / Pfeffer <span class="allergens">F 4, A, C, F, G, I, J</span></p>
      <p class="dish-desc">Pikante Sauce, <span class="allergens">F 4, A, C, F, G, I, J</span><br>verfeinert mit Weißwein</p>
    </article>

    <article class="dish">
      <h3 class="dish-name">Chef</h3>
      <span class="dish-price">23,-</span>
      <p class="dish-desc">verschiedene Fleischsorten in einer Tomaten-Knoblauch-Sauce mit Creme-fraiche verfeinert</p>
    </article>

    <article class="dish">
      <h3 class="dish-name">Skordo</h3>
      <span class="dish-price">23,-</span>
      <p class="dish-desc">verschiedene Fleischsorten mit Knoblauch, Paprika, Zwiebeln und Fetakäse</p>
    </article>
  </section>

  <section class="col-right">
    <h2 class="section-heading">Diese Gerichte<br>werden von Salat und<br><span>Reisbegleitet!</span></h2>

    <article class="dish">
      <h3 class="dish-name">Galopoula</h3>
      <span class="dish-price">21,5,-</span>
      <p class="dish-desc">Putengeschnetzeltes mit frischen Champignons, verfeinert mit einer</p>
    </article>

    <article class="dish">
      <h3 class="dish-name">Mon Amour</h3>
      <span class="dish-price">23,-</span>
      <p class="dish-desc">Hähnchenbrustfilet in einer<br>&nbsp;„Spezial-Fetasauce“</p>
    </article>

    <article class="dish">
      <h3 class="dish-name">Naxos</h3>
      <span class="dish-price">23,-</span>
      <p class="dish-desc">Rumpsteak Schweine-Putenfilet in „Spezial-Fetasauce“ mit Zucchini und Auberginenwürfel 24,-</p>
    </article>
  </section>

  <aside class="note-box">Tiganaki ist ein traditionelles griechisches Gericht, das aus Fleisch, Gemüse und einer Sauce besteht.</aside>

  <div class="brand">
    <span class="brand-mark"></span>
    <span class="brand-name">Olivara</span>
  </div>

  <p class="footer-note">Alle Preise in €. Änderungen mit Mehraufwand werden mit einem Aufpreis berechnet</p>
</main>
</body>
</html>
```